Light & Music Meditation (voucher)

I would like to attract new client to my center with a free voucher for a 15 minutes heart chakra session under my Tessaro Beam(brainwave entrainment) The lamp has more than 50 different program and a normal session takes up to an hour. With this voucher I offer a free 15 minutes session (opening heart chakra) More information on the producer site: www.tessarobeam-example.com
The voucher should be like a Postcard A6 printed on both sides not folded.

Therapy, wellness

```html
<!DOCTYPE html>
<html lang="en">
<head>
<meta charset="utf-8">
<title>Tessaro Beam – Free Voucher Postcard</title>
<link href="https://fonts.googleapis.com/css2?family=Montserrat:wght@400;500;600;800;900&family=Roboto+Condensed:wght@400&family=Oswald:wght@700&display=swap" rel="stylesheet">
<style>
  :root {
    --backdrop: #ffffff;
    --card-dark: #1f1f1f;
    --ink-black: #151515;
    --gold: #f3cf5c;
    --gold-deep: #c9a54a;
    --gold-light: #fbe27a;
    --paper: #ffffff;
    --text-light: #f2f2f2;
    --text-dark: #1b1b1b;
  }
  * { margin: 0; padding: 0; box-sizing: border-box; }
  html, body { width: 863px; height: 1200px; overflow: hidden; background: var(--backdrop); }
  body { position: relative; font-family: 'Montserrat', sans-serif; }

  .postcard {
    position: absolute;
    width: 747px; height: 1058px;
    transform-origin: 0 0;
    transform: scale(0.529);
    overflow: hidden;
    background: var(--card-dark);
  }
  .postcard--front { left: 26px; top: 320px; }
  .postcard--back { left: 442px; top: 320px; }

  .shapes { position: absolute; inset: 0; }
  .abs { position: absolute; }

  /* Brand */
  .brand-mark {
    position: absolute; width: 114px; height: 114px;
    border: 4px solid var(--gold); border-radius: 50%;
  }
  .brand-name { position: absolute; color: var(--gold); font-weight: 500; letter-spacing: 1px; }

  /* Front */
  .front-brand-mark { left: 53px; top: 33px; }
  .front-brand-name { left: 62px; top: 152px; font-size: 22px; }
  .kicker { left: 40px; top: 388px; font-size: 48px; font-weight: 400; color: var(--gold); letter-spacing: 0.5px; }
  .subhead { left: 40px; top: 470px; font-size: 30px; font-weight: 600; color: var(--text-light); }
  .headline { left: 36px; top: 498px; font-size: 84px; font-weight: 800; color: var(--gold); letter-spacing: 1px; line-height: 1; }
  .subhead--tail { top: 582px; }
  .intro {
    left: 34px; top: 656px; width: 430px;
    font-size: 22.5px; line-height: 27.3px; color: var(--text-light);
  }
  .benefits {
    left: 500px; top: 448px; list-style: none;
    font-family: 'Roboto Condensed', sans-serif; font-size: 22px; line-height: 26px; color: var(--text-dark);
  }
  .benefits li { position: relative; padding-left: 18px; }
  .benefits li::before {
    content: ""; position: absolute; left: 2px; top: 9px;
    width: 7px; height: 7px; border-radius: 50%; background: var(--gold);
  }

  /* Back */
  .research {
    left: 32px; top: 128px; width: 375px;
    font-size: 22.5px; line-height: 30.5px; color: var(--text-light);
  }
  .voucher { left: 33px; top: 636px; width: 682px; height: 380px; }
  .voucher-brand-mark { left: 55px; top: 665px; width: 80px; height: 80px; border-width: 3px; }
  .voucher-brand-name { left: 58px; top: 752px; font-size: 15px; }
  .voucher-title {
    left: 0; width: 747px; top: 658px; text-align: center; padding-left: 6px;
    font-size: 46px; font-weight: 900; color: var(--paper);
    text-shadow: 0 2px 4px rgba(0,0,0,0.45);
  }
  .voucher-duration {
    left: 0; width: 747px; top: 700px; text-align: center; padding-left: 6px;
    font-family: 'Oswald', sans-serif; font-size: 82px; font-weight: 700; color: var(--ink-black); line-height: 1.1;
  }
  .voucher-offer {
    left: 33px; width: 682px; top: 794px; text-align: center;
    font-size: 25px; line-height: 27px; color: var(--text-dark);
  }
  .voucher-rule { left: 70px; width: 608px; top: 852px; height: 1.5px; background: var(--paper); }
  .voucher-terms {
    left: 33px; width: 682px; top: 862px; text-align: center;
    font-size: 24px; line-height: 27px; color: var(--text-dark);
  }
</style>
</head>
<body>

<!-- Front side -->
<section class="postcard postcard--front">
  <svg class="shapes" viewBox="0 0 747 1058" aria-hidden="false">
    <defs>
      <linearGradient id="frontPhotoTone" x1="0" y1="0" x2="1" y2="1">
        <stop offset="0" stop-color="#0d1012"/>
        <stop offset="0.55" stop-color="#243238"/>
        <stop offset="1" stop-color="#101415"/>
      </linearGradient>
      <linearGradient id="goldBand" x1="0" y1="0" x2="1" y2="0">
        <stop offset="0" stop-color="#f8d765"/>
        <stop offset="1" stop-color="#d9b556"/>
      </linearGradient>
    </defs>
    <rect x="0" y="0" width="747" height="400" fill="url(#frontPhotoTone)" role="img" aria-label="Photo of a man lying back with closed eyes, wearing headphones, in dim blue light"/>
    <polygon points="0,277 495,388 0,362" fill="url(#goldBand)"/>
    <polygon points="0,362 495,390 453,1058 0,1058" fill="#1f1f1f"/>
    <polygon points="495,390 747,312 747,455" fill="url(#goldBand)"/>
    <polygon points="495,390 747,455 747,1058 453,1058" fill="#ffffff"/>
  </svg>

  <div class="brand-mark front-brand-mark"></div>
  <div class="brand-name front-brand-name">TESSARO</div>

  <h2 class="abs kicker">A PATH OF LIGHT</h2>
  <p class="abs subhead">BRAINWAVE ENTRAINMENT</p>
  <h1 class="abs headline">RAMPAGE</h1>
  <p class="abs subhead subhead--tail">OF HAPPINESS</p>

  <p class="abs intro">Your brain is made out of billions of cells called neurons. Neurons communicate with each other by firing electrical or/and hormonal signals. For performing different tasks different parts of your brain become activated and a cluster of neurons start communicating with each other by firing electrical pulses in a synchronized fashion to perform a certain task such as moving your hand, recalling a memory, and such.</p>

  <ul class="abs benefits">
    <li>Cognitive function</li>
    <li>Headaches</li>
    <li>Heart rate variability</li>
    <li>Pain relief</li>
    <li>PMS</li>
    <li>Stress</li>
    <li>Chronic fatigue</li>
    <li>Creativity</li>
    <li>Depression</li>
    <li>Hemispheric</li>
    <li>synchronization</li>
    <li>Insomnia</li>
    <li>Learning</li>
    <li>Lucid dreaming</li>
    <li>Meditation</li>
    <li>enhancement</li>
    <li>Memory</li>
    <li>Mood</li>
    <li>Relaxation</li>
    <li>Sleep improvement</li>
    <li>Targeted hemispheric</li>
    <li>changes</li>
  </ul>
</section>

<!-- Back side -->
<section class="postcard postcard--back">
  <svg class="shapes" viewBox="0 0 747 1058">
    <defs>
      <linearGradient id="backPhotoTone" x1="0" y1="0" x2="1" y2="1">
        <stop offset="0" stop-color="#3a2a24"/>
        <stop offset="0.45" stop-color="#a8684a"/>
        <stop offset="1" stop-color="#3b3848"/>
      </linearGradient>
      <linearGradient id="backFade" x1="0" y1="0" x2="1" y2="0">
        <stop offset="0" stop-color="#1f1f1f" stop-opacity="1"/>
        <stop offset="1" stop-color="#1f1f1f" stop-opacity="0"/>
      </linearGradient>
      <linearGradient id="voucherGold" x1="0" y1="0" x2="1" y2="1">
        <stop offset="0" stop-color="#d8b25a"/>
        <stop offset="0.6" stop-color="#f2cf66"/>
        <stop offset="1" stop-color="#fbe07a"/>
      </linearGradient>
    </defs>
    <rect x="0" y="0" width="747" height="620" fill="#1a1a1a"/>
    <rect x="400" y="0" width="347" height="620" fill="url(#backPhotoTone)" role="img" aria-label="Photo of a calm bald man in profile with eyes closed, wearing over-ear headphones"/>
    <rect x="400" y="0" width="90" height="620" fill="url(#backFade)"/>
    <rect x="33" y="636" width="682" height="3" fill="#ffffff"/>
    <path d="M33,639 H715 V920 Q715,955 680,955 H400 L375,1015 L350,955 H68 Q33,955 33,920 Z" fill="url(#voucherGold)"/>
  </svg>

  <p class="abs research">In 1981, researcher Elian Rossvik discovered that 15 minutes of stimulation with isochronic tones enhanced biofeedback protocols for bruxism (grinding of teeth). They did this by increasing muscle relaxation superior than standalone biofeedback. Brainwave entrainment is different from biofeedback in that it does not allow the person to consciously control their brainwave state.</p>

  <div class="brand-mark voucher-brand-mark"></div>
  <div class="brand-name voucher-brand-name">TESSARO</div>

  <p class="abs voucher-title">FREE VOUCHER</p>
  <p class="abs voucher-duration">15 MINUTES</p>
  <p class="abs voucher-offer">heart chakra session under my<br>Tessaro Beam(brainwave entrainment)</p>
  <div class="abs voucher-rule"></div>
  <p class="abs voucher-terms">A normal session takes up to an hour.<br>With this voucher I offer a free 15 minutes session<br>(opening heart chakra)</p>
</section>

</body>
</html>
```